Marvista Coffee Roasters needs a coffee bag design for retail sales

We need an outstanding design for a retail coffee bag to package our outstanding craft roasted coffee beans. We have our logo and need to incorporate that into an original, overall design that includes areas for text boxes on the front, back and sides. We can provide the text when we select the design. One text box on the front will remain blank. This is where we will adhere a label that will describe the particular coffee in the package. And blank text box on the back to print a bar code.
These are our preliminary thoughts and are open minded to other options.

We would like a clean, "classy" design (think wine label). We are not sold on any particular color at this time for the bag or for the text but would design to work on different color bags(pleasing, eyecatching). We want the design to convey that our coffee is an exceptional product -- creative, sustainable, organic, socially and environmentally responsible and with remarkable taste.
Updates

I hope you understand that we are not trying to create a new label. We want to get the bags printed with a design that includes our logo. The design would need a space on the front for a small sticker or label that we can print ourselves giving the origin or blend of each particular coffee.(text only) I like the idea you showed us of the back text box with the rough edge like our logo. We wont print bar codes on the bags. if needed we will affix bar code stickers to the bottom of the bag. There is a website that has a template for creating bag designs.  You can access the templates by creating a free account. We would use the 12/16 oz gusseted bags. Here is a link. http://www.pouchwerk.example/

Target Market(s)

sophisticated coffee drinkers ---similar to wine connoiseurs

Industry/Entity Type

Retail

Requirements
Must have
• our Logo --font is Trajen Pro --- except for the J...which was created to have the up-curl
Nice to have
• something unique
Should not have
• goofy cartoon-like cliche--common coffee related images and colors

```html
<!DOCTYPE html>
<html lang="en">
<head>
<meta charset="utf-8">
<title>Marvista Coffee Roasters – Retail Bag Front</title>
<link rel="stylesheet" href="https://fonts.googleapis.com/css2?family=Cinzel:wght@400;500&display=swap">
<style>
  :root {
    --backdrop: #d9d9d9;
    --bag-white: #ffffff;
    --bag-mist: #eef7f6;
    --bag-aqua: #c4e4e1;
    --bag-teal: #93cbc7;
    --bag-deep-teal: #6fb4b0;
    --art-sea: #3ab2a4;
    --art-lime: #d3de97;
    --art-green: #2f9f86;
    --art-forest: #16352c;
    --type-green: #1f8a5f;
    --mark-ink: #1b2622;
    --seal-band: rgba(150, 180, 180, 0.45);
  }

  html, body {
    margin: 0;
    width: 1200px;
    height: 1200px;
    overflow: hidden;
    background: var(--backdrop);
  }

  .canvas {
    position: relative;
    width: 1200px;
    height: 1200px;
  }

  .bag-front {
    position: absolute;
    left: 300px;
    top: 75px;
    width: 600px;
    height: 1060px;
    border-radius: 12px 12px 6px 6px;
    overflow: hidden;
    background: linear-gradient(90deg,
      var(--bag-mist) 0%,
      var(--bag-white) 30%,
      var(--bag-aqua) 55%,
      var(--bag-teal) 82%,
      var(--bag-deep-teal) 100%);
  }

  .seal-band {
    position: absolute;
    left: 0;
    top: 0;
    width: 100%;
    height: 70px;
    background:
      repeating-linear-gradient(180deg, transparent 0 9px, rgba(255,255,255,0.4) 9px 11px),
      var(--seal-band);
  }

  .botanical-artwork {
    position: absolute;
    left: 0;
    top: 0;
    width: 600px;
    height: 1060px;
  }

  .tagline {
    position: absolute;
    left: 755px;
    top: 185px;
    height: 462px;
    margin: 0;
    writing-mode: vertical-rl;
    transform: rotate(180deg);
    text-align: end;
    font-family: "Cinzel", "Times New Roman", serif;
    font-weight: 500;
    font-size: 51px;
    line-height: 51px;
    color: var(--type-green);
  }

  .tagline span { display: block; }

  .brand {
    position: absolute;
    left: 640px;
    top: 765px;
    width: 236px;
    text-align center;
    text-align: center;
    color: var(--mark-ink);
    font-family: "Cinzel", "Times New Roman", serif;
    font-weight: 500;
  }

  .brand-square {
    display: block;
    width: 200px;
    height: 198px;
    margin: 0 0 16px 18px;
    border: 8px solid var(--mark-ink);
    box-sizing: border-box;
  }

  .brand-name {
    margin: 0;
    font-size: 44px;
    line-height: 46px;
  }

  .brand-descriptor {
    margin: 0;
    font-size: 23px;
    line-height: 30px;
    letter-spacing: 1px;
  }
</style>
</head>
<body>
  <main class="canvas">
    <section class="bag-front">
      <svg class="botanical-artwork" viewBox="0 0 600 1060" role="img" aria-label="Flowing botanical artwork of teal, lime and deep green ribbons, grasses and a dotted arc rising from an ink splash">
        <defs>
          <linearGradient id="artwork-tone" x1="0" y1="0" x2="0" y2="1">
            <stop offset="0" stop-color="var(--art-sea)" stop-opacity="0.7"/>
            <stop offset="0.35" stop-color="var(--art-lime)" stop-opacity="0.75"/>
            <stop offset="0.6" stop-color="var(--art-green)" stop-opacity="0.85"/>
            <stop offset="0.85" stop-color="var(--art-forest)" stop-opacity="0.95"/>
            <stop offset="1" stop-color="var(--art-forest)" stop-opacity="0.8"/>
          </linearGradient>
          <linearGradient id="artwork-fade" x1="0" y1="0" x2="1" y2="0">
            <stop offset="0" stop-color="var(--art-sea)" stop-opacity="0.35"/>
            <stop offset="1" stop-color="var(--art-sea)" stop-opacity="0"/>
          </linearGradient>
        </defs>
        <path d="M0,120 C120,260 260,380 430,140 L440,160 C300,420 160,400 0,330 Z" fill="url(#artwork-fade)"/>
        <path d="M0,0 L120,0 C170,200 210,400 250,560 C290,720 330,880 390,1010 L420,1060 L0,1060 Z" fill="url(#artwork-tone)"/>
      </svg>

      <div class="seal-band"></div>
    </section>

    <h2 class="tagline">
      <span>Premium Coffee</span>
      <span>100% Arabica</span>
    </h2>

    <div class="brand">
      <span class="brand-square"></span>
      <p class="brand-name">MARVISTA</p>
      <p class="brand-descriptor">COFFEE ROASTERS</p>
    </div>
  </main>
</body>
</html>
```